" Nosso corpo jurídico é constituído por profissionais com vasta experiência na advocacia. A reunião desses profissionais e o amadurecimento de um ideal comum, resultaram na criação de um grupo comprometido com a prestação de serviços jurídicos. Estamos aptos a atender, com eficiência, agilidade e qualidade, atuando em equipe ou individualmente para solução do seu problema, por meio de métodos eficientes e dinâmicos. "

```html
<!DOCTYPE html>
<html lang="pt-BR">
<head>
<meta charset="UTF-8">
<title>Moreira Lacerda &amp; Fontes Advogados — Cartão de visita</title>
<link rel="stylesheet" href="https://fonts.googleapis.com/css2?family=Cormorant+Garamond:wght@500&family=Montserrat:wght@400;500&display=swap">
<style>
  :root {
    --page: #e9e9e7;
    --card-white: #ffffff;
    --brown: #3a2f2b;
    --brown-deep: #2e2522;
    --tan: #c9965f;
    --tan-light: #d7a874;
    --mark-faint: #f1f1f1;
    --ink-light: #e8dccd;
  }
  * { margin: 0; padding: 0; box-sizing: border-box; }
  html, body { width: 1200px; height: 1200px; overflow: hidden; }
  body {
    background: var(--page);
    display: flex;
    flex-direction: column;
    align-items: center;
    justify-content: center;
    gap: 70px;
    font-family: "Montserrat", sans-serif;
  }
  .card {
    position: relative;
    width: 900px;
    height: 500px;
    overflow: hidden;
    box-shadow: 0 6px 18px rgba(0,0,0,0.12);
  }

  /* Front */
  .card-front { background: var(--card-white); }
  .front-edge {
    position: absolute;
    left: 0; right: 0; bottom: 0;
    height: 22px;
    display: flex;
  }
  .front-edge .edge-dark { flex: 0 0 72%; background: var(--brown); }
  .front-edge .edge-tan { flex: 1; background: var(--tan); }
  .front-mark {
    position: absolute;
    right: 110px;
    top: 110px;
    width: 250px;
    height: 250px;
    background: var(--mark-faint);
  }

  /* Back */
  .card-back { background: var(--brown); }
  .back-flap { position: absolute; inset: 0; width: 100%; height: 100%; }
  .firm {
    position: absolute;
    left: 80px;
    top: 205px;
    display: flex;
    align-items: center;
    gap: 22px;
  }
  .firm-square {
    width: 54px;
    height: 54px;
    border: 4px solid var(--tan);
  }
  .firm-name {
    font-family: "Cormorant Garamond", serif;
    font-weight: 500;
    color: var(--tan);
    font-size: 25px;
    line-height: 1.15;
    letter-spacing: 1.5px;
    text-transform: uppercase;
  }
  .contact-list {
    position: absolute;
    left: 520px;
    top: 255px;
    list-style: none;
    display: flex;
    flex-direction: column;
    gap: 11px;
  }
  .contact-item {
    display: flex;
    align-items: center;
    gap: 12px;
    color: var(--ink-light);
    font-size: 15px;
    letter-spacing: 0.3px;
  }
  .contact-icon {
    width: 20px;
    height: 20px;
    flex: 0 0 20px;
  }
</style>
</head>
<body>

<section class="card card-front" aria-label="Frente do cartão">
  <div class="front-mark" role="img" aria-label="Marca do escritório em tom claro"></div>
  <div class="front-edge">
    <span class="edge-dark"></span>
    <span class="edge-tan"></span>
  </div>
</section>

<section class="card card-back" aria-label="Verso do cartão">
  <svg class="back-flap" viewBox="0 0 900 500" preserveAspectRatio="none" aria-hidden="true">
    <path d="M150 0 L900 0 L900 225 Q880 240 860 232 Z" fill="var(--brown-deep)"/>
    <path d="M190 0 L900 0 L900 200 Q885 214 865 206 Z" fill="var(--tan)"/>
  </svg>

  <div class="firm">
    <span class="firm-square"></span>
    <p class="firm-name">Moreira Lacerda<br>&amp; Fontes Advogados</p>
  </div>

  <ul class="contact-list">
    <li class="contact-item">
      <svg class="contact-icon" viewBox="0 0 20 20"><circle cx="10" cy="10" r="10" fill="var(--tan)"/><rect x="5" y="6.5" width="10" height="7" fill="none" stroke="var(--brown)" stroke-width="1.4"/><path d="M5 7 L10 11 L15 7" fill="none" stroke="var(--brown)" stroke-width="1.4"/></svg>
      contato@mlfadv.com.br
    </li>
    <li class="contact-item">
      <svg class="contact-icon" viewBox="0 0 20 20"><circle cx="10" cy="10" r="10" fill="var(--tan)"/><circle cx="10" cy="10" r="5" fill="none" stroke="var(--brown)" stroke-width="1.4"/><path d="M5 10 H15 M10 5 Q7 10 10 15 M10 5 Q13 10 10 15" fill="none" stroke="var(--brown)" stroke-width="1.2"/></svg>
      www.mlfadv.com.br
    </li>
    <li class="contact-item">
      <svg class="contact-icon" viewBox="0 0 20 20"><circle cx="10" cy="10" r="10" fill="var(--tan)"/><path d="M7 5 L9 5 L10 8 L8.5 9 Q9.5 11.5 11 12 L12 10.5 L15 11.5 L15 13.5 Q10 15 6 9 Q5.5 6.5 7 5 Z" fill="var(--brown)"/></svg>
      (21) 4000-1234
    </li>
    <li class="contact-item">
      <svg class="contact-icon" viewBox="0 0 20 20"><circle cx="10" cy="10" r="10" fill="var(--tan)"/><rect x="7" y="4.5" width="6" height="11" rx="1" fill="none" stroke="var(--brown)" stroke-width="1.4"/><circle cx="10" cy="13.3" r="0.8" fill="var(--brown)"/></svg>
      (21) 98000-1234
    </li>
    <li class="contact-item">
      <svg class="contact-icon" viewBox="0 0 20 20"><circle cx="10" cy="10" r="10" fill="var(--tan)"/><path d="M10 15.5 Q5.5 10.5 5.5 8.5 A4.5 4.5 0 0 1 14.5 8.5 Q14.5 10.5 10 15.5 Z" fill="var(--brown)"/><circle cx="10" cy="8.5" r="1.6" fill="var(--tan)"/></svg>
      Rua das Acácias, 120
    </li>
  </ul>
</section>

</body>
</html>
```